"Every Lantern Still Burning" Sermon Series Design

Needing a design for our church's next sermon series titled "Every Lantern Still Burning" where we will discuss the need for unity, diversity, love and clarity. Looking for a 1920 x 1080 (or higher res) editable and layered file (PSD or AI) so that we can reformat the design to work on social, screens, lower thirds and various print and online mediums. We will also need to have access to the font files so that we can make resize and tweak as needed. We like the idea of using a globe or map of the world as the backdrop with the words overtop. Or, the idea of creating a bunch of newspaper clippings (generic, so that they can't actually be read) and making the shape of a heart. See attached examples. This website will give you an idea of our previous sermon series designs so you can have an idea of our style (but, feel free to help us advance the ball on something more aligned with current design trends): https://www.brinmoorfellowship.church/series

Examples use red, but stay away from a ton of red. If you're gonna major in a color, use blue or something in that family.

Must haves:
Title: Every Lantern Still Burning
Tagline : (TBD - use some Lorem Ipsum as a placeholder and we will fill in later)
Our Logo (attached) (small towards bottom is standard - only use solid colors for logo - preferably just solid black or white)

Industry/Entity Type

Church

Font styles to use
Serif
Sans Serif

Requirements
Must have
• Title: Every Lantern Still Burning
Nice to have
• We like the idea of using a globe or map of the world as the backdrop with the words overtop. Or, the idea of creating a bunch of newspaper clippings (generic, so that they can't actually be read) and making the shape of a heart. See attached examples.

If you're gonna major on a color, stick with blue or something close.
Should not have
• Don't use red as the primary color (example we sent has red, but stay away from it)

```html
<!DOCTYPE html>
<html lang="en">
<head>
<meta charset="utf-8">
<title>Every Lantern Still Burning — Sermon Series</title>
<link href="https://fonts.googleapis.com/css2?family=Oswald:wght@500&display=swap" rel="stylesheet">
<style>
  :root {
    --sky-top: #0f2452;
    --sky-mid: #2c4f8f;
    --horizon-glow: #e9e4f0;
    --ridge-far: #5e7fb8;
    --ridge-mid: #34528c;
    --valley-deep: #1b2c58;
    --foreground-dark: #0f1a38;
    --moss-tint: #2f4a4a;
    --ink-white: #ffffff;
  }
  html, body {
    margin: 0;
    padding: 0;
    width: 1200px;
    height: 675px;
    overflow: hidden;
    background: var(--foreground-dark);
  }
  .series-canvas {
    position: relative;
    width: 1200px;
    height: 675px;
    overflow: hidden;
    font-family: "Oswald", "Arial Narrow", sans-serif;
  }
  .landscape-backdrop {
    position: absolute;
    inset: 0;
    background:
      radial-gradient(ellipse 60% 30% at 25% 75%, rgba(47, 74, 74, 0.55), transparent 70%),
      radial-gradient(ellipse 40% 35% at 92% 80%, rgba(10, 16, 36, 0.7), transparent 70%),
      linear-gradient(180deg,
        var(--sky-top) 0%,
        var(--sky-mid) 12%,
        #9fb4d8 14.5%,
        var(--horizon-glow) 15%,
        #8aa4d4 16.5%,
        var(--ridge-far) 22%,
        var(--ridge-mid) 38%,
        var(--valley-deep) 62%,
        var(--foreground-dark) 100%);
  }
  .title-frame {
    position: absolute;
    left: 380px;
    top: 61px;
    width: 441px;
    height: 553px;
    box-sizing: border-box;
    border: 1px solid var(--ink-white);
  }
  .series-title {
    position: absolute;
    left: 380px;
    top: 61px;
    width: 441px;
    height: 553px;
    margin: 0;
    display: flex;
    flex-direction: column;
    justify-content: center;
    align-items: center;
    gap: 24px;
    color: var(--ink-white);
    font-weight: 500;
    font-size: 66px;
    line-height: 1;
    text-transform: uppercase;
    text-shadow: 0 2px 10px rgba(0, 0, 0, 0.35);
  }
  .series-title .title-line {
    display: block;
    letter-spacing: 26px;
    padding-left: 26px;
  }
  .church-mark {
    position: absolute;
    left: 777px;
    top: 570px;
    width: 88px;
    height: 88px;
    box-sizing: border-box;
    border-radius: 50%;
    border: 3px solid var(--ink-white);
    background: var(--valley-deep);
  }
  .church-name {
    position: absolute;
    right: 432px;
    top: 624px;
    margin: 0;
    color: var(--ink-white);
    font-weight: 500;
    font-size: 13px;
    letter-spacing: 3px;
    text-transform: uppercase;
  }
</style>
</head>
<body>
  <main class="series-canvas">
    <div class="landscape-backdrop" role="img" aria-label="Moonlit panorama of misty blue mountain ranges stretching to a glowing horizon"></div>
    <div class="title-frame"></div>
    <h1 class="series-title">
      <span class="title-line">Every</span>
      <span class="title-line">Lantern</span>
      <span class="title-line">Still</span>
      <span class="title-line">Burning</span>
    </h1>
    <div class="church-mark"></div>
    <p class="church-name">Brinmoor Fellowship</p>
  </main>
</body>
</html>
```